Accounting business needs business card

I have a business card but need something better. I want the colour changed and the design to be better. I have uploaded a picture of my new sign that is grey in colour, i would like to incorporate these colours.

```html
<!DOCTYPE html>
<html lang="en">
<head>
<meta charset="UTF-8">
<title>Nova Tax – Business Card</title>
<link href="https://fonts.googleapis.com/css2?family=Montserrat:wght@500;600&family=Quicksand:wght@400;500;700&display=swap" rel="stylesheet">
<style>
  :root {
    --page: #ffffff;
    --card-front: #858585;
    --card-back: #ececec;
    --ink: #1d1d1d;
    --ink-soft: #333333;
    --white: #ffffff;
    --accent: #44bb94;
    --badge-blue: #1f4f9e;
    --badge-gold: #f2c21b;
    --badge-sky: #2aa7df;
    --shadow: rgba(0, 0, 0, 0.45);
  }
  * { margin: 0; padding: 0; box-sizing: border-box; }
  html, body {
    width: 940px; height: 1200px; overflow: hidden;
    background: var(--page);
  }
  .canvas { position: relative; width: 940px; height: 1200px; }

  .card {
    position: absolute; left: 174px; width: 608px; height: 364px;
    box-shadow: 6px 7px 8px var(--shadow);
    overflow: hidden;
  }
  .card--front { top: 195px; background: var(--card-front); }
  .card--back  { top: 658px; background: var(--card-back); }

  /* Front */
  .front-mark {
    position: absolute; left: 253px; top: 120px;
    width: 84px; height: 84px; border-radius: 50%;
    border: 2.5px solid var(--white);
  }
  .front-name {
    position: absolute; left: 0; right: 0; top: 218px; text-align: center;
    font-family: "Montserrat", sans-serif; font-weight: 500;
    font-size: 27px; letter-spacing: 7px; color: var(--white);
    padding-left: 7px;
  }
  .front-web {
    position: absolute; left: 0; right: 0; top: 305px; text-align: center;
    font-family: "Montserrat", sans-serif; font-weight: 600;
    font-size: 13.5px; letter-spacing: 1.6px; color: var(--white);
  }

  /* Back */
  .divider { position: absolute; left: 0; top: 0; }
  .brand-mark {
    position: absolute; left: 124px; top: 115px;
    width: 84px; height: 84px; border-radius: 50%;
    border: 2.5px solid var(--ink);
  }
  .brand-name {
    position: absolute; left: 36px; width: 250px; top: 211px; text-align: center;
    font-family: "Montserrat", sans-serif; font-weight: 600;
    font-size: 24px; letter-spacing: 5.5px; color: var(--ink);
  }
  .badges { position: absolute; left: 62px; top: 288px; display: flex; align-items: center; }
  .badge-member {
    width: 79px; height: 35px; background: var(--badge-blue); position: relative;
  }
  .badge-member::after {
    content: ""; position: absolute; right: 3px; top: 3px;
    width: 24px; height: 29px; background: var(--badge-gold);
  }
  .badge-note {
    margin-left: 14px; width: 82px;
    font-family: "Quicksand", sans-serif; font-weight: 500;
    font-size: 8.5px; line-height: 11px; color: var(--ink);
  }
  .badge-partner {
    margin-left: 4px; width: 33px; height: 33px; border-radius: 50%;
    background: var(--badge-sky);
  }

  .person { position: absolute; right: 43px; top: 36px; text-align: right; }
  .person-name {
    font-family: "Quicksand", sans-serif; font-weight: 700;
    font-size: 25px; letter-spacing: 1px; color: var(--accent);
  }
  .person-credentials, .person-role {
    font-family: "Quicksand", sans-serif; font-weight: 500;
    font-size: 10.5px; line-height: 13px; color: var(--ink-soft);
  }
  .person-credentials { margin-top: 4px; }

  .contacts { position: absolute; left: 325px; top: 173px; list-style: none; }
  .contact {
    display: flex; align-items: center; height: 27px;
    font-family: "Quicksand", sans-serif; font-weight: 500;
    font-size: 15px; letter-spacing: 0.6px; color: var(--ink);
  }
  .contact-icon { width: 27px; height: 16px; margin-right: 7px; flex: none; }
</style>
</head>
<body>
<main class="canvas">

  <section class="card card--front" aria-label="Card front">
    <div class="front-mark" aria-hidden="true"></div>
    <p class="front-name">NOVA TAX</p>
    <p class="front-web">www.novatax.com.au</p>
  </section>

  <section class="card card--back" aria-label="Card back">
    <svg class="divider" width="608" height="364" viewBox="0 0 608 364" aria-hidden="true">
      <polygon points="283,0 301,0 301,148 292,160 283,148" fill="var(--accent)"/>
      <polygon points="292,258 301,270 301,364 283,364 283,270" fill="var(--accent)"/>
    </svg>

    <div class="brand-mark" aria-hidden="true"></div>
    <p class="brand-name">NOVA TAX</p>

    <div class="badges">
      <div class="badge-member" aria-hidden="true"></div>
      <p class="badge-note">Nova Tax is a Certified Business</p>
      <div class="badge-partner" aria-hidden="true"></div>
    </div>

    <div class="person">
      <p class="person-name">Liam Porter</p>
      <p class="person-credentials">CPA,MTX,BCOM, (Acc &amp; Fin)</p>
      <p class="person-role">Taxation and Business Accountant</p>
    </div>

    <ul class="contacts">
      <li class="contact">
        <svg class="contact-icon" viewBox="0 0 27 16" aria-hidden="true">
          <polygon points="0,0 21,0 27,8 21,16 0,16" fill="var(--accent)"/>
          <path d="M6 3.5 q-1.5 1 0 4.5 q2 3.5 5 5 q2 0.8 3-1 l-2.2-1.8 -1.3 1 q-2-1-3.2-3.3 l1-1.2 -1.6-2.4 z" fill="var(--white)"/>
        </svg>
        0412 555 308
      </li>
      <li class="contact">
        <svg class="contact-icon" viewBox="0 0 27 16" aria-hidden="true">
          <polygon points="0,0 21,0 27,8 21,16 0,16" fill="var(--accent)"/>
          <rect x="4" y="4" width="14" height="9" fill="none" stroke="var(--white)" stroke-width="1.3"/>
          <polyline points="4,4 11,9.5 18,4" fill="none" stroke="var(--white)" stroke-width="1.3"/>
        </svg>
        liam@novatax.com.au
      </li>
      <li class="contact">
        <svg class="contact-icon" viewBox="0 0 27 16" aria-hidden="true">
          <polygon points="0,0 21,0 27,8 21,16 0,16" fill="var(--accent)"/>
          <circle cx="11" cy="8" r="5.3" fill="none" stroke="var(--white)" stroke-width="1.2"/>
          <ellipse cx="11" cy="8" rx="2.3" ry="5.3" fill="none" stroke="var(--white)" stroke-width="1"/>
          <line x1="5.7" y1="8" x2="16.3" y2="8" stroke="var(--white)" stroke-width="1"/>
        </svg>
        www.novatax.com.au
      </li>
    </ul>
  </section>

</main>
</body>
</html>
```